Luxury Ayurvedic Hair Oil logo and package design

We need a logo and package design for our Ayurvedic and natural hair growth oil. Our company, Velmora, is the premier luxury Ayurvedic beauty brand, bringing ancient East-Indian natural and botanic health and beauty products to the US market. Our first major product - Velmora Hair Growth Oil - is a coconut oil based product that was developed by tribes in the Southern State of Kerala that includes ancient herbs like Gooseberry, Indigo, Indian Aloe, Balloon Vine and Brahmi.

The design should be catered to the high-end luxury market (minimal design, minimal text, fonts that invoke a sense of luxury). The primary colors should be deep blue for the packaging and gold for the characters (it's in the name - Velmora). We are looking to sell our products in Brenvale and Tolland Pryce and require packaging that is in line with products sold at these high-end retailers.

The final logo design and packaging should communicate luxury and the ancient wisdom of far-eastern traditions.

Target Market(s)

Velmora's main target is women who value fashionable/quality skincare, beauty, and fragrance products and are open to a medium to high price range. These women love uniqueness in brand and products that cannot be found elsewhere. They are looking for the next new "it" item that will take their haircare and beauty regiment to the next level.

Industry/Entity Type

Hair And Beauty

Font styles to use
Serif

Colors
2f73b3
ffc214

Requirements
Must have
• Must use deep blue (royal blue) background and gold text (to align with brand name). Must use luxurious fonts
Nice to have
• Flowers or other natural symbols, pictures that blend well with the product theme

```html
<!DOCTYPE html>
<html lang="en">
<head>
<meta charset="utf-8">
<title>Velmora Hair Growth Oil – Carton Panels</title>
<link rel="stylesheet" href="https://fonts.googleapis.com/css2?family=Cinzel:wght@600;700&family=Open+Sans:wght@400;600&display=swap">
<style>
  :root {
    --bg: #e9edf3;
    --navy: #221f6e;
    --navy-deep: #17155a;
    --gold: #d9b25a;
    --gold-light: #f3dc98;
    --gold-dark: #a8782c;
    --tagline: #4a63c4;
  }
  html, body {
    margin: 0;
    width: 1200px;
    height: 675px;
    overflow: hidden;
    background: var(--bg);
  }
  .canvas {
    position: relative;
    width: 1200px;
    height: 675px;
    display: flex;
    align-items: center;
    justify-content: center;
    gap: 0;
  }
  .panel {
    position: relative;
    height: 560px;
    background: radial-gradient(ellipse at 50% 45%, var(--navy) 0%, var(--navy-deep) 100%);
    box-sizing: border-box;
    overflow: hidden;
  }
  .panel::before, .panel::after {
    content: "";
    position: absolute;
    left: 0; right: 0;
    height: 16px;
    background: linear-gradient(90deg, var(--gold-dark), var(--gold-light) 45%, var(--gold) 70%, var(--gold-dark));
  }
  .panel::before { top: 0; }
  .panel::after { bottom: 0; }

  .panel-side { width: 150px; border-right: 1px solid rgba(217,178,90,0.35); }
  .panel-front { width: 300px; }
  .panel-back { width: 150px; border-left: 1px solid rgba(217,178,90,0.35); }

  .ornament {
    position: absolute;
    left: 50%;
    transform: translateX(-50%);
    width: 230px;
    height: 110px;
  }
  .ornament-top {
    top: 16px;
    border-radius: 0 0 115px 115px;
    background: radial-gradient(ellipse at 50% 0%, rgba(217,178,90,0.75), rgba(168,120,44,0.35) 60%, rgba(168,120,44,0) 78%);
  }
  .ornament-bottom {
    bottom: 16px;
    width: 200px;
    height: 100px;
    border-radius: 100px 100px 0 0;
    background: radial-gradient(ellipse at 50% 100%, rgba(217,178,90,0.75), rgba(168,120,44,0.35) 60%, rgba(168,120,44,0) 78%);
  }
  .brand {
    position: absolute;
    left: 0; right: 0;
    text-align: center;
    font-family: "Cinzel", serif;
    font-weight: 600;
    color: var(--gold);
    letter-spacing: 0.08em;
  }
  .brand-mark {
    display: block;
    width: 14px; height: 14px;
    margin: 0 auto 6px;
    border-radius: 50%;
    border: 1.5px solid var(--gold);
  }
  .brand-main { top: 150px; font-size: 14px; }
  .brand-foot { bottom: 78px; font-size: 11px; }

  .title {
    position: absolute;
    top: 205px;
    left: 0; right: 0;
    text-align: center;
    margin: 0;
    font-family: "Cinzel", serif;
    font-weight: 700;
    font-size: 27px;
    line-height: 1.15;
    color: var(--gold-light);
    background: linear-gradient(180deg, var(--gold-light), var(--gold) 60%, var(--gold-dark));
    -webkit-background-clip: text;
    background-clip: text;
    -webkit-text-fill-color: transparent;
  }
  .rule {
    display: block;
    width: 180px;
    height: 1.5px;
    margin: 10px auto;
    background: linear-gradient(90deg, rgba(217,178,90,0), var(--gold) 30%, var(--gold) 70%, rgba(217,178,90,0));
  }
  .tagline {
    position: absolute;
    top: 312px;
    left: 0; right: 0;
    text-align: center;
    margin: 0;
    font-family: "Open Sans", sans-serif;
    font-size: 11px;
    line-height: 1.45;
    color: var(--tagline);
  }
  .origin {
    position: absolute;
    bottom: 60px;
    left: 0; right: 0;
    text-align: center;
    font-family: "Open Sans", sans-serif;
    font-size: 8px;
    color: var(--tagline);
  }

  .info {
    position: absolute;
    top: 40px; left: 16px; right: 16px;
    font-family: "Open Sans", sans-serif;
    font-size: 10px;
    line-height: 1.55;
    color: var(--tagline);
  }
  .info p { margin: 0 0 16px; }
  .volume {
    position: absolute;
    bottom: 40px; left: 0; right: 0;
    text-align: center;
    font-family: "Open Sans", sans-serif;
    font-size: 16px;
    color: var(--tagline);
  }
  .panel-back .brand-main { top: 230px; font-size: 13px; }
</style>
</head>
<body>
<main class="canvas">
  <section class="panel panel-side" aria-label="Carton side panel">
    <div class="info">
      <p>Stimulate slow &amp; inactive hair follicles and unclogs blocked pores. Soothes &amp; conditions the scalp, promotes longer, thicker and healthier hair.</p>
      <p>Crafted from ayurvedic natural ancient herbs including Gooseberry, Indigo, Indian Aloe, Balloon Vine and Brahmi.</p>
    </div>
    <div class="volume">50ml</div>
  </section>

  <section class="panel panel-front" aria-label="Carton front panel">
    <div class="ornament ornament-top" role="img" aria-label="Gold mandala ornament"></div>
    <div class="brand brand-main"><span class="brand-mark"></span>VELMORA</div>
    <h1 class="title"><span class="rule"></span>Hair<br>Growth Oil<span class="rule"></span></h1>
    <p class="tagline">Southern State of Kerala's<br>Ancient Tribes Legacy</p>
    <div class="brand brand-foot"><span class="brand-mark"></span>VELMORA</div>
    <div class="origin">Made in USA</div>
    <div class="ornament ornament-bottom" role="img" aria-label="Gold mandala ornament"></div>
  </section>

  <section class="panel panel-back" aria-label="Carton end panel">
    <div class="brand brand-main"><span class="brand-mark"></span>VELMORA</div>
  </section>
</main>
</body>
</html>
```